professional business card

A Clean looking business card for a money transfer company. Our company is call Velorix= Transfer + Send = Transcend (next level)
to show professionalism as well as some effects to show digital tech.

1 side to have position, name and address
2 side to have company name and show that we provide money exchange and cross-border money transfer

Target Market(s)

Remittance companies and high net worth individuals

Industry/Entity Type

Finance

Contact Information for Business Card

Name, address, email, title, services- money exchange and cross-border remittance

Requirements
Nice to have
• Digital age feel

```html
<!DOCTYPE html>
<html lang="en">
<head>
<meta charset="utf-8">
<title>Velorix Business Card</title>
<link href="https://fonts.googleapis.com/css2?family=Lato:wght@400;700;900&display=swap" rel="stylesheet">
<style>
  :root {
    --navy: #263340;
    --cyan: #63d2df;
    --white: #ffffff;
    --ink: #1f2a36;
    --muted: #4a5560;
    --page: #e9ecef;
  }
  * { margin: 0; padding: 0; box-sizing: border-box; }
  html, body { width: 1200px; height: 952px; overflow: hidden; }
  body {
    background: var(--page);
    font-family: "Lato", Arial, sans-serif;
    position: relative;
  }
  .card {
    position: absolute;
    left: 250px;
    width: 700px;
    height: 400px;
    border-radius: 26px;
    overflow: hidden;
    box-shadow: 0 10px 30px rgba(0,0,0,0.18);
  }
  .card-front { top: 50px; background: var(--navy); }
  .card-back { top: 502px; background: var(--white); }
  .card-shapes { position: absolute; inset: 0; }

  .brand {
    position: absolute;
    display: flex;
    align-items: center;
    gap: 18px;
  }
  .brand-dot {
    width: 40px; height: 40px;
    border-radius: 50%;
    background: var(--cyan);
  }
  .brand-name {
    font-weight: 700;
    letter-spacing: 4px;
    line-height: 1;
  }
  .card-front .brand { left: 150px; top: 128px; }
  .card-front .brand-name { font-size: 72px; color: var(--white); }
  .card-back .brand { left: 250px; top: 60px; }
  .card-back .brand-dot { width: 32px; height: 32px; }
  .card-back .brand-name { font-size: 56px; color: var(--ink); }

  .pill {
    position: absolute;
    border-radius: 18px;
    display: flex;
    align-items: center;
    justify-content: center;
    white-space: nowrap;
  }
  .tagline {
    left: 110px; top: 263px;
    width: 360px; height: 34px;
    background: var(--white);
    border: 2px solid var(--navy);
    color: var(--ink);
    font-weight: 700;
    font-size: 16px;
  }
  .address {
    left: 40px; top: 284px;
    width: 390px; height: 30px;
    background: var(--cyan);
    color: var(--white);
    font-size: 14px;
    font-weight: 700;
  }

  .person { position: absolute; left: 50px; top: 190px; }
  .person-name {
    font-size: 26px;
    font-weight: 700;
    letter-spacing: 1px;
    color: var(--ink);
    text-transform: uppercase;
  }
  .person-name .surname { color: var(--cyan); }
  .person-title {
    font-size: 18px;
    color: var(--muted);
    text-align: right;
    margin-top: 2px;
  }

  .contacts {
    position: absolute;
    left: 440px; top: 218px;
    list-style: none;
  }
  .contacts li {
    display: flex;
    align-items: center;
    gap: 10px;
    font-size: 16px;
    color: var(--muted);
    margin-bottom: 10px;
  }
  .contact-icon {
    width: 22px; height: 22px;
    border-radius: 4px;
    background: var(--cyan);
    display: flex;
    align-items: center;
    justify-content: center;
    flex: none;
  }
</style>
</head>
<body>

<section class="card card-front">
  <svg class="card-shapes" viewBox="0 0 700 400" aria-hidden="true">
    <path d="M0,280 H470 C492,280 498,300 506,330 C514,360 520,372 540,372 H700 V400 H0 Z" fill="var(--cyan)"/>
    <path d="M0,270 H470 C500,270 506,296 514,326 C522,354 528,362 546,362 H700" fill="none" stroke="var(--white)" stroke-width="2"/>
  </svg>
  <div class="brand">
    <span class="brand-dot"></span>
    <span class="brand-name">VELORIX</span>
  </div>
  <div class="pill tagline">Money Exchange And Cross-border Remittance</div>
</section>

<section class="card card-back">
  <svg class="card-shapes" viewBox="0 0 700 400" aria-hidden="true">
    <path d="M0,300 H430 C455,300 462,320 470,345 C478,366 486,372 505,372 H700 V400 H0 Z" fill="var(--navy)"/>
    <path d="M0,292 H430 C462,292 470,316 478,340 C486,360 492,364 510,364 H700" fill="none" stroke="var(--cyan)" stroke-width="2"/>
  </svg>
  <div class="brand">
    <span class="brand-dot"></span>
    <span class="brand-name">VELORIX</span>
  </div>
  <div class="person">
    <div class="person-name">Daniel M. <span class="surname">Harlow</span></div>
    <div class="person-title">Managing Director</div>
  </div>
  <ul class="contacts">
    <li>
      <span class="contact-icon">
        <svg width="14" height="14" viewBox="0 0 24 24"><path d="M6.6 10.8a15 15 0 0 0 6.6 6.6l2.2-2.2a1 1 0 0 1 1-.25 11.4 11.4 0 0 0 3.6.57 1 1 0 0 1 1 1V20a1 1 0 0 1-1 1A17 17 0 0 1 3 4a1 1 0 0 1 1-1h3.5a1 1 0 0 1 1 1c0 1.25.2 2.45.57 3.6a1 1 0 0 1-.25 1z" fill="var(--white)"/></svg>
      </span>
      +00 987 654 32
    </li>
    <li>
      <span class="contact-icon">
        <svg width="14" height="14" viewBox="0 0 24 24"><rect x="2" y="5" width="20" height="14" rx="1" fill="none" stroke="var(--white)" stroke-width="2"/><path d="M2 6l10 7 10-7" fill="none" stroke="var(--white)" stroke-width="2"/></svg>
      </span>
      hello@velorixpay.com
    </li>
    <li>
      <span class="contact-icon">
        <svg width="14" height="14" viewBox="0 0 24 24"><path d="M5 3l14 8-6 1.5L10 19z" fill="var(--white)"/></svg>
      </span>
      www.velorixpay.com
    </li>
  </ul>
  <div class="pill address">1270 Linden Park Avenue Arlington, VA 22201</div>
</section>

</body>
</html>
```